Website Design - for Energy Efficiency company - large corporate feel

Hi there,
Thanks for checking out this project!
We're a UK based energy efficiency business. We arrange for energy efficient systems to be fitted in people's houses (i.e. efficient boilers, solar panels etc.) However, we do not install them ourselves as we have accredited installers who install on our behalf. Therefore the website should appeal to these businesses and have a very professional corporate feel. The final design should communicate that we are a financially safe large corporation.
Our existing website should not be used for inspiration as the style and content are very outdated (it was from a time when were installers - which we no longer are).
The new website design should use the greens from our logo, however I don't want the site saturated in this colour.
I'm really open to your chosen layout and therefore I'm not a huge fan of including links to websites I like - as I don't want to limit your own creativity. However, I would like it to look corporate (but not too boring and unimaginative).
So here's a few links to websites that I feel give a feel of financially safe / large corporate etc. Although you certainly don't have to design with this style / layout in mind:
http://www.brelvanhub.org.uk/advice
http://www.tolvenrise.co.uk/
http://www.qpwd.org.uk/
http://www.wendrowkeyplot.co.uk/
http://www.ruvasto.co.uk/ (very bad design but looks corporate)
http://www.pellarwatt.org.uk/
http://www.vq.co.uk/ (looks corporate but too busy and boring)
http://www.quellisto.co.uk/business/index.htm
http://www.dormavel.com/
https://www.ostrevan.com/en/index.html
The site is for 4 different audiences:
Consumers | Businesses | Public Sector | Installers
Therefore, it's important that there is some form of way of splitting the site up into these sections (almost like 4 websites in 1). Each section will then have the navigation menu with 7 links.
I've attached our logo (company-logo.jpg) and another logo design we have to display inline with regulations (blue-pact-logo.jpg).
Happy designing, and thank you!

```html
<!DOCTYPE html>
<html lang="en">
<head>
<meta charset="utf-8">
<title>Leafmore Energy – Consumers</title>
<link rel="stylesheet" href="https://fonts.googleapis.com/css2?family=Ubuntu:wght@300;400;500;700&display=swap">
<style>
:root{
  --green:#5a8f29;
  --green-dark:#4e7f22;
  --green-light:#8dc63f;
  --lime-text:#2f3f14;
  --blue:#2c6c9a;
  --grey-band:#e6e6e6;
  --grey-line:#c9dcab;
  --text:#333;
  --muted:#555;
  --icon:#a3a3a3;
  --white:#fff;
}
*{box-sizing:border-box;margin:0;padding:0}
html,body{width:891px;height:1200px;overflow:hidden;background:var(--white)}
body{position:relative;font-family:"Ubuntu",sans-serif;color:var(--text)}
a{text-decoration:none;color:inherit}
.abs{position:absolute}

/* audience tabs */
.audience-bar{left:0;top:0;width:891px;height:42px;background:var(--grey-band);border-bottom:1px solid var(--green-light)}
.audience-tabs{left:124px;top:14px;display:flex;font-size:11.5px;color:#888}
.audience-tabs a{padding:6px 7px;height:28px}
.audience-tabs a.is-active{background:var(--white);color:#222;border:1px solid var(--green-light);border-bottom:none;height:28px;padding:6px 7px}

/* header */
.brand{left:124px;top:64px;display:flex;align-items:center;gap:8px}
.brand-dot{width:34px;height:34px;border-radius:50%;background:var(--green)}
.brand-name{font-size:26px;font-weight:500;color:var(--green);letter-spacing:.2px}
.phone{right:123px;top:68px;text-align:right}
.phone-number{display:flex;align-items:center;gap:4px;font-size:24px;font-weight:300;color:var(--green)}
.phone-label{font-size:10.5px;font-weight:500;color:#222;margin-top:3px}

/* main nav */
.main-nav{left:124px;top:135px;width:644px;height:35px;background:var(--green);border-radius:3px;display:flex}
.main-nav a{display:flex;align-items:center;justify-content:center;color:var(--white);font-size:12.5px;border-right:1px solid #6ea03a}
.main-nav a:last-child{border-right:none}

/* hero */
.hero{left:124px;top:185px;width:644px;height:273px;border-radius:3px;overflow:hidden;
  background:linear-gradient(160deg,#d9552f 0%,#c9472a 35%,#8aa3c9 55%,#c84a2c 80%,#7a8f3a 100%)}
.hero-card{left:21px;top:97px;width:287px;height:156px;background:var(--white);border-radius:3px;padding:12px 20px}
.hero-title{font-size:28px;font-weight:300;color:#333;line-height:33px}
.hero-title strong{font-weight:500;display:block}
.hero-text{font-size:11.5px;line-height:16.5px;color:#444;margin-top:10px;font-weight:300}
.hero-link{left:20px;bottom:14px;font-size:9.5px;font-weight:500;color:var(--green)}
.hero-dots{right:11px;bottom:11px;display:flex;gap:5px}
.hero-dots span{width:6px;height:6px;border-radius:50%;background:#bbb}
.hero-dots span.is-current{background:var(--green)}

/* intro */
.intro{left:124px;top:496px;width:278px}
.intro h1{font-size:19px;font-weight:500;color:var(--green);margin-bottom:8px}
.intro p{font-size:9.6px;line-height:16.5px;color:#444;font-weight:300}
.read-more{font-size:10.5px;font-weight:500;color:var(--green)}
.intro .read-more{display:block;margin-top:14px}
.intro-mark{left:434px;top:525px;width:128px;height:122px;border-radius:50%;background:var(--green)}

/* side boxes */
.pact-box{left:604px;top:480px;width:164px;height:212px;background:var(--green-light);border-radius:2px;padding:12px 14px;color:var(--lime-text)}
.pact-box h2{font-size:14.5px;font-weight:500;margin-bottom:6px}
.pact-box p{font-size:9.3px;line-height:17.8px;font-weight:300}
.pact-box a{display:block;margin-top:6px;font-size:9.5px;font-weight:500;text-decoration:underline}
.reviews-box{left:604px;top:713px;width:164px;height:177px;background:var(--blue);border-radius:2px;padding:12px 14px;color:var(--white)}
.reviews-box h2{font-size:14.5px;font-weight:500;line-height:16px;margin-bottom:6px}
.reviews-box p{font-size:9.3px;line-height:17.8px;font-weight:300}
.reviews-box .customer{text-align:right;font-size:9.5px;font-weight:500;margin-top:4px}
.reviews-box a{display:block;margin-top:11px;font-size:9.5px;font-weight:500}

/* services */
.service{top:705px;width:120px}
.service svg{display:block;height:64px}
.service h3{font-size:14.5px;font-weight:500;color:#222;margin-top:20px}
.service p{font-size:8.3px;line-height:16.5px;color:#333;margin-top:6px;font-weight:300}
.service .read-more{display:block;margin-top:8px;font-size:9.5px}

/* badges */
.badges{left:124px;top:940px;width:644px;height:36px;display:flex;justify-content:space-between;align-items:center}
.badge{background:#bdbdbd}

/* footer */
.footer{left:0;top:1008px;width:891px;height:192px;background:var(--grey-band);border-top:1px solid var(--grey-line)}
.footer-col{top:26px;font-size:8.3px;line-height:16.5px;color:#666}
.footer-col h4{font-size:8.3px;font-weight:500;color:#333}
.copyright{left:124px;top:155px;font-size:8.3px;color:#555}
</style>
</head>
<body>

<div class="abs audience-bar">
  <nav class="abs audience-tabs">
    <a class="is-active" href="#">Consumers</a>
    <a href="#">Businesses</a>
    <a href="#">Public Sector</a>
    <a href="#">Installers</a>
  </nav>
</div>

<header>
  <div class="abs brand">
    <span class="brand-dot"></span>
    <span class="brand-name">Leafmore Energy</span>
  </div>
  <div class="abs phone">
    <div class="phone-number">
      <svg width="20" height="20" viewBox="0 0 24 24"><path fill="#5a8f29" d="M6.6 10.8a15.1 15.1 0 0 0 6.6 6.6l2.2-2.2c.3-.3.7-.4 1-.2 1.1.4 2.3.6 3.6.6.6 0 1 .4 1 1V20c0 .6-.4 1-1 1A17 17 0 0 1 3 4c0-.6.4-1 1-1h3.5c.6 0 1 .4 1 1 0 1.3.2 2.5.6 3.6.1.3 0 .7-.2 1l-2.3 2.2z"/></svg>
      0800 413 7726
    </div>
    <div class="phone-label">CALL US NOW</div>
  </div>
</header>

<nav class="abs main-nav">
  <a href="#" style="width:78px">Home</a>
  <a href="#" style="width:92px">About Us</a>
  <a href="#" style="width:102px">Blue Pact</a>
  <a href="#" style="width:65px">ECO</a>
  <a href="#" style="width:96px">Landlords</a>
  <a href="#" style="width:108px">Renewables</a>
  <a href="#" style="width:103px">Contact Us</a>
</nav>

<section class="abs hero" role="img" aria-label="Photo of solar panels fitted on a red tiled house roof under a blue sky">
  <div class="abs hero-card">
    <h2 class="hero-title">Power your home <strong>for free</strong></h2>
    <p class="hero-text">Generate electricity and income for your home with Solar Panels</p>
    <a class="abs hero-link" href="#">&gt;&nbsp; LEARN MORE</a>
    <div class="abs hero-dots"><span class="is-current"></span><span></span><span></span><span></span></div>
  </div>
</section>

<section class="abs intro">
  <h1>Lorem ipsum dolor sit amet</h1>
  <p>Lorem ipsum dolor sit amet, consectetur adipisicing elit, sed do eiusmod tempor incididunt ut labore et dolore magna aliqua. Ut enim ad minim veniam, quis nostrud exercitation ullamco laboris nisi ut aliquip ex ea commodo consequat. Duis aute irure dolor in reprehenderit in voluptate velit esse cillum dolore eu fugiat nulla pariatur. Excepteur sint occaecat cupidatat non proident, sunt in culpa qui officia deserunt mollit anim id est laborum.</p>
  <a class="read-more" href="#">&gt; Read more</a>
</section>
<div class="abs intro-mark"></div>

<aside class="abs pact-box">
  <h2>Blue Pact</h2>
  <p>The Blue Pact gives people the opportunity to transform their homes by paying for energy efficient home improvements with the savings on their energy bills. It is available to homeowners, tenants and tenants.</p>
  <a href="#">&gt; Read more</a>
</aside>

<aside class="abs reviews-box">
  <h2>Customer<br>Reviews</h2>
  <p>Lorem ipsum dolor sit amet, consectetur adipiscing elit, sed do eiusmod tempor incididunt ut labore et dolore magna aliqua.</p>
  <div class="customer">CUSTOMER NAME</div>
  <a href="#">&gt; Read more reviews</a>
</aside>

<article class="abs service" style="left:124px">
  <svg width="60" height="64" viewBox="0 0 60 64"><path fill="#a3a3a3" d="M30 2C22 16 16 30 22 46c2 6 6 10 8 14 2-4 6-8 8-14 6-16 0-30-8-44zM4 26c2 14 6 26 20 34-6-10-8-22-20-34zm52 0c-12 12-14 24-20 34 14-8 18-20 20-34z"/></svg>
  <h3>ECO</h3>
  <p>Lorem ipsum dolor sit amet, consectetur adipiscing elit. Non igitur bene.</p>
  <a class="read-more" href="#">&gt; Read more</a>
</article>

<article class="abs service" style="left:282px">
  <svg width="60" height="64" viewBox="0 0 60 64"><circle cx="30" cy="30" r="26" fill="none" stroke="#a3a3a3" stroke-width="3"/><rect x="24" y="10" width="3" height="10" fill="#a3a3a3"/><rect x="33" y="10" width="3" height="10" fill="#a3a3a3"/><path fill="#a3a3a3" d="M17 20h26v5H17zm3 6h20l-4 12H24z"/><rect x="27" y="38" width="6" height="18" fill="#a3a3a3"/></svg>
  <h3>Landlords</h3>
  <p>Lorem ipsum dolor sit amet, consectetur adipiscing elit. Non igitur bene.</p>
  <a class="read-more" href="#">&gt; Read more</a>
</article>

<article class="abs service" style="left:439px">
  <svg width="60" height="64" viewBox="0 0 60 64"><path fill="none" stroke="#a3a3a3" stroke-width="7" d="M14 42A20 20 0 0 1 30 10M46 22A20 20 0 0 1 30 54"/><path fill="#a3a3a3" d="M28 2l10 8-10 8zM32 46l-10 8 10 8z"/><circle cx="30" cy="32" r="5" fill="#a3a3a3"/></svg>
  <h3>Renewables</h3>
  <p>Lorem ipsum dolor sit amet, consectetur adipiscing elit. Non igitur bene.</p>
  <a class="read-more" href="#">&gt; Read more</a>
</article>

<div class="abs badges" aria-label="Accreditation badges">
  <span class="badge" style="width:62px;height:28px;border-radius:3px"></span>
  <span class="badge" style="width:76px;height:26px;border-radius:3px"></span>
  <span class="badge" style="width:42px;height:28px;border-radius:50%"></span>
  <span class="badge" style="width:32px;height:32px;border-radius:50%"></span>
  <span class="badge" style="width:28px;height:30px;border-radius:3px"></span>
  <span class="badge" style="width:85px;height:30px;border-radius:3px"></span>
</div>

<footer class="abs footer">
  <div class="abs footer-col" style="left:124px"><h4>For Consumers</h4>Insulation<br>Heating<br>Solar</div>
  <div class="abs footer-col" style="left:233px"><h4>For Businesses</h4>Businesses<br>Housebuilders<br>Housing Associations</div>
  <div class="abs footer-col" style="left:342px"><h4>For Public Sector</h4>Local Authorities<br>Education<br>Other</div>
  <div class="abs footer-col" style="left:454px"><h4>For Installers</h4>Lorem<br>Ipsum<br>Dolor<br>Sit amet</div>
  <div class="abs footer-col" style="left:563px"><h4>About Us</h4>Who are we?<br>History<br>Community<br>News</div>
  <div class="abs footer-col" style="left:673px"><h4>Help</h4>FAQs<br>Glossary<br>Terms &amp; Conditions<br>Cookie &amp; Privacy Policy<br>Sitemap</div>
  <p class="abs copyright">Copyright © Leafmore Energy 2013 - All rights reserved.</p>
</footer>

</body>
</html>
```